Marlowvane Services Website Design

We have most content but require a professional design. We have a logo already and will need it utilized along with several of the photos from the attached documentation.
First page should have our mission and Vision and the synapsis provided in the word document. Visitors will be prompted to select from one of our 3 divisions from this page.
Each division will have the same list of tabs : About, Services, Safety, Careers and Contact.
Photos on each divisions page should be representative of the divisions offerings. The word doc attached contains the requested content and we are open to edits that would complement and fill the website.
I like the Tornwick site www.tornwick-example.com - they are our competition so cant be modeled directly after this.
Please include prompts to request quote at each service page. align the format of the geotechnical page to the other 2 divisions.
I used chat gpt for some of the content so will need it optimized for SCO.

```html
<!DOCTYPE html>
<html lang="en">
<head>
<meta charset="utf-8">
<title>Marlowvane Services</title>
<link href="https://fonts.googleapis.com/css2?family=Bebas+Neue&family=Poppins:wght@400;500;600;700&display=swap" rel="stylesheet">
<style>
:root{
  --red:#ed1c24;
  --black:#000;
  --footer:#161616;
  --white:#fff;
  --ink:#333;
  --muted:#666;
  --faint:#9a9a9a;
}
*{margin:0;padding:0;box-sizing:border-box}
html,body{width:758px;height:1200px;overflow:hidden;background:var(--black)}
body{position:relative;font-family:'Poppins',sans-serif;color:var(--white)}
.hero-block{position:absolute;left:0;top:0;width:278px;height:320px;background:var(--red)}
.brand{position:absolute;left:63px;top:14px;font-weight:700;font-size:16px;letter-spacing:2px;color:var(--white)}
.hero-photo{position:absolute;left:63px;top:63px;width:305px;height:363px;
  background:linear-gradient(160deg,#a99173 0%,#8a7258 45%,#6f5a44 100%)}
.headline{position:absolute;left:386px;top:124px;font-family:'Bebas Neue',sans-serif;font-weight:400;font-size:72px;line-height:62px;color:#f5f5f5;letter-spacing:0.5px}
.section-title{position:absolute;left:0;width:758px;text-align:center;font-family:'Bebas Neue',sans-serif;font-weight:400;font-size:28px;line-height:28px;color:var(--white)}
.mission-title{top:510px}
.mission-text{position:absolute;left:92px;top:551px;width:574px;text-align:center;font-size:10px;line-height:15.8px;color:var(--white)}
.division-title{top:687px}
.division-lead{position:absolute;left:120px;top:729px;width:518px;text-align:center;font-size:13.5px;line-height:21.5px;color:var(--white)}
.card{position:absolute;top:797px;width:189px;height:260px;background:var(--white)}
.card-photo{position:absolute;left:12.5px;top:14px;width:164px;height:97px}
.card-title{position:absolute;left:12.5px;top:929px;font-family:'Bebas Neue',sans-serif;font-weight:400;font-size:15px;color:var(--ink);letter-spacing:0.2px}
.card .card-title{top:131px}
.card-text{position:absolute;left:12.5px;top:158px;width:166px;font-size:6.6px;line-height:12.7px;color:var(--muted)}
.card-button{position:absolute;left:12.5px;top:214px;width:164px;height:38px;background:var(--red);color:var(--white);
  font-size:9px;font-weight:600;display:flex;align-items:center;justify-content:center}
.card-button.short{width:160px}
.footer{position:absolute;left:0;top:1149px;width:758px;height:51px;background:var(--footer)}
.footer-brand{position:absolute;left:56px;top:15px;font-weight:700;font-size:15px;letter-spacing:2px;color:var(--red)}
.copyright{position:absolute;left:0;width:758px;top:18px;text-align:center;font-size:9.5px;color:var(--faint)}
.social{position:absolute;top:21px;width:7px;height:7px;border-radius:50%;background:var(--white)}
</style>
</head>
<body>
  <div class="hero-block"></div>
  <div class="brand">MARLOWVANE</div>

  <div class="hero-photo" role="img" aria-label="Aerial view of a white crane truck parked on a dirt yard"></div>

  <h1 class="headline">SAFETY.<br>QUALITY.<br>SERVICE.</h1>

  <h2 class="section-title mission-title">MISSION &amp; VISION</h2>
  <p class="mission-text">At Marlowvane Services, we are dedicated to delivering unparalleled aerial access, geotechnical drilling, and service and maintenance solutions, consistently exceeding our clients' expectations. Our vision is to be the leading provider of aerial access, geotechnical drilling, and service solutions, setting the standard for excellence in safety, efficiency, and environmental stewardship.</p>

  <h2 class="section-title division-title">SELECT DIVISION</h2>
  <p class="division-lead">Choose from one of our three specialized divisions to explore our services tailored to your industry needs:</p>

  <div class="card" style="left:83px">
    <div class="card-photo" role="img" aria-label="Aerial lift truck parked on a gravel road in a forest" style="background:linear-gradient(180deg,#5f7a4a 0%,#8aa36a 45%,#9a9488 75%,#7d7367 100%)"></div>
    <h3 class="card-title">AERIAL ACCESS</h3>
    <p class="card-text">Providing comprehensive aerial access solutions for efficient project execution.</p>
    <div class="card-button">Elevate Your Projects</div>
  </div>

  <div class="card" style="left:285px">
    <div class="card-photo" role="img" aria-label="Red drilling rig beside a water tower on a grassy lot" style="background:linear-gradient(180deg,#4f86c8 0%,#8fb4de 45%,#c9cfd2 62%,#8e8a5c 80%,#7a7550 100%)"></div>
    <h3 class="card-title">GEOTECHNICAL DRILLING</h3>
    <p class="card-text">Delivering advanced geotechnical drilling services to support ground investigations and analysis.</p>
    <div class="card-button">Dig Deeper</div>
  </div>

  <div class="card" style="left:487px">
    <div class="card-photo" role="img" aria-label="Aerial lift boom reaching a wind turbine against blue sky" style="background:linear-gradient(200deg,#2f6fc4 0%,#4a86d6 55%,#9bb8de 100%)"></div>
    <h3 class="card-title">RENEWABLE ENERGY SERVICES</h3>
    <p class="card-text">Offering specialized services to support the renewable energy sector's infrastructure development.</p>
    <div class="card-button short">Power Your Future</div>
  </div>

  <footer class="footer">
    <div class="footer-brand">MARLOWVANE</div>
    <p class="copyright">© 2024 by Marlowvane Services Inc.</p>
    <span class="social" style="left:598px"></span>
    <span class="social" style="left:615px"></span>
    <span class="social" style="left:632px"></span>
  </footer>
</body>
</html>
```